Commercial Insurance Agency needs a design for a trade show retractable display.

We need a design for a retractable banner or display for a trade show. We are a commercial insurance agency that specializes in placing and servicing workers comp insurance for large companies. We want to use our company colors which are orange, grey and charcoal.

Font styles to use
Sans Serif

Requirements
Must have
• Our orange color that is on the style sheet should be the secondary color...we don't want the whole thing to be orange

```html
<!DOCTYPE html>
<html lang="en">
<head>
<meta charset="utf-8">
<title>KEEL90 Trade Show Banner</title>
<link rel="stylesheet" href="https://fonts.googleapis.com/css2?family=Montserrat:wght@400;500;600;700;800&display=swap">
<style>
  :root {
    --charcoal: #454545;
    --charcoal-deep: #3a3a3a;
    --orange: #f05a24;
    --grey-light: #e4e4e4;
    --text-soft: #dcdcdc;
    --white: #ffffff;
    --backdrop: #e9e9e9;
  }
  * { margin: 0; padding: 0; box-sizing: border-box; }
  html, body { width: 1200px; height: 1000px; overflow: hidden; }
  body {
    background: var(--backdrop);
    font-family: "Montserrat", Arial, sans-serif;
    position: relative;
  }
  .banner {
    position: absolute;
    left: 385px; top: 60px;
    width: 430px; height: 880px;
    background: var(--charcoal);
    overflow: hidden;
    box-shadow: 0 6px 18px rgba(0,0,0,0.18);
  }
  .banner-shapes { position: absolute; inset: 0; }
  .brand {
    position: absolute; top: 36px; left: 0; width: 100%;
    text-align: center;
  }
  .brand-name {
    font-weight: 800; font-size: 40px; line-height: 48px;
    color: var(--white); letter-spacing: 1px;
  }
  .service {
    position: absolute; width: 430px; height: 130px;
  }
  .service-badge { position: absolute; width: 124px; height: 124px; }
  .service-text { position: absolute; }
  .service-title {
    color: var(--orange); font-weight: 700; font-size: 19px;
    text-transform: uppercase; line-height: 1.1; margin-bottom: 3px;
  }
  .service-desc {
    color: var(--text-soft); font-weight: 500; font-size: 13px;
    line-height: 1.3; letter-spacing: 0.2px;
  }
  .service--compliance { top: 462px; }
  .service--compliance .service-badge { left: 35px; top: 0; }
  .service--compliance .service-text { left: 176px; top: 36px; width: 215px; }
  .service--claims { top: 575px; }
  .service--claims .service-badge { left: 270px; top: 0; }
  .service--claims .service-text { right: 174px; top: 40px; width: 200px; text-align: right; }
  .service--profit { top: 693px; }
  .service--profit .service-badge { left: 35px; top: 0; }
  .service--profit .service-text { left: 170px; top: 36px; width: 220px; }
  .footer-band {
    position: absolute; left: 0; bottom: 0; width: 100%; height: 40px;
    background: var(--orange);
    border-top: 3px solid var(--white);
    display: flex; align-items: center; justify-content: center;
    color: var(--white); font-weight: 600; font-size: 17px;
  }
</style>
</head>
<body>
  <div class="banner">
    <svg class="banner-shapes" width="430" height="880" viewBox="0 0 430 880">
      <defs>
        <linearGradient id="photoTone" x1="0" y1="0" x2="1" y2="1">
          <stop offset="0" stop-color="#dfe6ec"/>
          <stop offset="0.5" stop-color="#c9ced3"/>
          <stop offset="1" stop-color="#8f949a"/>
        </linearGradient>
      </defs>
      <rect x="0" y="80" width="430" height="420" fill="url(#photoTone)" role="img" aria-label="Photo of two smiling business professionals in a meeting at an office desk"/>
      <path d="M0,0 H430 V140 C380,142 360,108 300,100 C220,92 90,96 0,88 Z" fill="var(--white)"/>
      <path d="M0,0 H430 V130 C380,134 360,100 300,92 C220,84 90,92 0,84 Z" fill="var(--charcoal)"/>
      <path d="M0,470 C120,440 300,425 430,405 V880 H0 Z" fill="var(--white)"/>
      <path d="M0,480 C120,452 300,436 430,417 V880 H0 Z" fill="var(--charcoal)"/>
    </svg>

    <div class="brand">
      <span class="brand-name">KEEL90</span>
    </div>

    <div class="service service--compliance">
      <svg class="service-badge" viewBox="0 0 124 124">
        <circle cx="62" cy="62" r="60" fill="var(--orange)"/>
        <circle cx="62" cy="62" r="54" fill="var(--charcoal-deep)"/>
        <circle cx="62" cy="62" r="51" fill="var(--white)"/>
        <circle cx="62" cy="62" r="45" fill="var(--grey-light)"/>
        <circle cx="56" cy="56" r="19" fill="none" stroke="var(--orange)" stroke-width="9" stroke-dasharray="7 4.9"/>
        <circle cx="56" cy="56" r="15" fill="var(--orange)"/>
        <circle cx="56" cy="56" r="6" fill="var(--grey-light)"/>
        <line x1="60" y1="60" x2="82" y2="82" stroke="var(--grey-light)" stroke-width="11" stroke-linecap="round"/>
        <line x1="60" y1="60" x2="82" y2="82" stroke="var(--orange)" stroke-width="6" stroke-linecap="round"/>
      </svg>
      <div class="service-text">
        <h2 class="service-title">Compliance</h2>
        <p class="service-desc">Training and Certifications HR and Safety Onsite Compliance Audits</p>
      </div>
    </div>

    <div class="service service--claims">
      <svg class="service-badge" viewBox="0 0 124 124">
        <circle cx="62" cy="62" r="60" fill="var(--orange)"/>
        <circle cx="62" cy="62" r="54" fill="var(--charcoal-deep)"/>
        <circle cx="62" cy="62" r="51" fill="var(--white)"/>
        <circle cx="62" cy="62" r="45" fill="var(--grey-light)"/>
        <path d="M40,58 A23,23 0 0 1 78,45" fill="none" stroke="var(--orange)" stroke-width="7"/>
        <polygon points="72,34 90,42 76,56" fill="var(--orange)"/>
        <path d="M84,66 A23,23 0 0 1 46,79" fill="none" stroke="var(--orange)" stroke-width="7"/>
        <polygon points="52,90 34,82 48,68" fill="var(--orange)"/>
      </svg>
      <div class="service-text">
        <h2 class="service-title">Claims</h2>
        <p class="service-desc">Immediate, Ongoing Injury and Claims Management</p>
      </div>
    </div>

    <div class="service service--profit">
      <svg class="service-badge" viewBox="0 0 124 124">
        <circle cx="62" cy="62" r="60" fill="var(--orange)"/>
        <circle cx="62" cy="62" r="54" fill="var(--charcoal-deep)"/>
        <circle cx="62" cy="62" r="51" fill="var(--white)"/>
        <circle cx="62" cy="62" r="45" fill="var(--grey-light)"/>
        <g fill="none" stroke="var(--orange)" stroke-width="3.5" stroke-linecap="round">
          <path d="M54,76 C54,68 46,64 46,55 A16,16 0 0 1 78,55 C78,64 70,68 70,76 Z"/>
          <line x1="55" y1="82" x2="69" y2="82"/>
          <line x1="57" y1="88" x2="67" y2="88"/>
          <line x1="62" y1="26" x2="62" y2="32"/>
          <line x1="38" y1="36" x2="42" y2="40"/>
          <line x1="86" y1="36" x2="82" y2="40"/>
          <line x1="28" y1="56" x2="34" y2="56"/>
          <line x1="90" y1="56" x2="96" y2="56"/>
        </g>
      </svg>
      <div class="service-text">
        <h2 class="service-title">Profit Leams</h2>
        <p class="service-desc">Detect and Correct Profit Leaks Inherent in Every Work Comp Program that Drives the Cost</p>
      </div>
    </div>

    <div class="footer-band">keel90.com</div>
  </div>
</body>
</html>
```